IT Company needs a new Flyer Design

We are an expanding IT company based in Perth, Western Australia. When we first opened we produced a small flyer internally and letter box dropped to 100 business in our area (we are located in a newly developed and ever increasing commercial district). We had a good hit ratio and picked up a handful of local companies.
5 years has passed and we have grown significantly, we now feel the time is right to get out there are start canvasing the hundreds of new business which have opened in past couple of years in our area. We are the largest company of our type in the area by far with 10 staff (any other IT support companies in the area are 1 or 2 man bands).
Our Key strength is our Complete IT Management approach, giving our clients a complete rang of services from traditional IT Services (Support, Servers, Workstations, Printers), Electrical (Data Cabling, All Electrical Work, Exit Light Testing, Testing and Tagging), Web Division (SEO, Websites, Copy Writing etc), Offsite Backup and Cloud Solutions, Phone systems and Security systems integrating CCTV and Access Control.
I have attached the first flyer we produced internally, as well as Company Logo's etc. Feel free to re-write the text, the text still gets the message across, but happy for it to have some create flare added.
The aim of this brochure is to introduce ourselves and also the fact that we are in the local area.
The target market will be business owners.
Business

```html
<!DOCTYPE html>
<html lang="en">
<head>
<meta charset="utf-8">
<title>Ridgeway Networking – Complete IT Management</title>
<link rel="stylesheet" href="https://fonts.googleapis.com/css2?family=Open+Sans:wght@300;400;600;700;800&display=swap">
<style>
  :root {
    --slate: #5f7284;
    --slate-text: #5b6e80;
    --body-grey: #8b9097;
    --white: #ffffff;
    --photo-light: #f4f5f6;
    --photo-mid: #c9ced3;
    --photo-deep: #9aa3ab;
    --contact-panel: rgba(255,255,255,0.14);
  }
  html, body {
    margin: 0;
    padding: 0;
    width: 860px;
    height: 1200px;
    overflow: hidden;
    background: var(--white);
  }
  .flyer {
    position: relative;
    width: 860px;
    height: 1200px;
    overflow: hidden;
    font-family: "Open Sans", Arial, sans-serif;
    background: var(--white);
  }
  .hero-photo {
    position: absolute;
    left: 0; top: 0;
    width: 860px; height: 444px;
    background:
      radial-gradient(ellipse 220px 260px at 470px 300px, rgba(154,163,171,0.55) 0%, rgba(154,163,171,0) 100%),
      radial-gradient(ellipse 260px 120px at 720px 260px, rgba(154,163,171,0.45) 0%, rgba(154,163,171,0) 100%),
      linear-gradient(90deg, #dfe2e5 0%, var(--photo-light) 30%, #e9ebed 70%, #d6dadd 100%);
  }
  .masthead {
    position: absolute;
    left: 58px; top: 50px;
    color: var(--slate-text);
  }
  .masthead-name {
    margin: 0;
    font-weight: 800;
    font-size: 66px;
    line-height: 66px;
    letter-spacing: 0;
  }
  .masthead-sub {
    display: block;
    margin-top: 6px;
    font-weight: 700;
    font-size: 31px;
    line-height: 36px;
    letter-spacing: 0.5px;
  }
  .masthead-tagline {
    margin: 6px 0 0;
    font-weight: 300;
    font-size: 25px;
    line-height: 30px;
  }
  .brand-mark {
    position: absolute;
    left: 60px; top: 482px;
    display: flex;
    align-items: center;
    gap: 12px;
    color: var(--slate-text);
    font-weight: 700;
    font-size: 22px;
    letter-spacing: 0.5px;
  }
  .brand-square {
    width: 62px; height: 62px;
    background: var(--slate-text);
  }
  .content-band {
    position: absolute;
    left: 0; top: 626px;
    width: 860px; height: 574px;
    background: var(--slate);
  }
  .column-title {
    position: absolute;
    top: 580px;
    width: 236px;
    margin: 0;
    text-align: center;
    color: var(--slate-text);
    font-weight: 700;
    font-size: 18px;
    letter-spacing: 0.5px;
  }
  .card {
    position: absolute;
    top: 626px;
    width: 236px;
    height: 286px;
    background: var(--white);
    box-shadow: 3px 4px 6px rgba(0,0,0,0.28);
    box-sizing: border-box;
    padding: 6px 8px 0 10px;
    color: var(--body-grey);
    font-weight: 300;
    font-size: 10.2px;
    line-height: 15.3px;
  }
  .col-1 { left: 57px; }
  .col-2 { left: 315px; }
  .col-3 { left: 572px; }
  .card p { margin: 0 0 15px; }
  .service-list {
    list-style: none;
    margin: 0 0 15px;
    padding: 0 0 0 2px;
    color: var(--slate-text);
    font-weight: 600;
    font-size: 11px;
    line-height: 15.3px;
  }
  .service-list li {
    display: flex;
    align-items: center;
    gap: 7px;
  }
  .tick { width: 10px; height: 10px; flex: none; }
  .section-heading {
    margin: 0;
    color: var(--white);
    font-weight: 700;
    font-size: 25px;
    letter-spacing: 0.5px;
  }
  .about {
    position: absolute;
    left: 60px; top: 970px;
    width: 445px;
    color: var(--white);
  }
  .about p {
    margin: 12px 0 0;
    font-weight: 300;
    font-size: 9.6px;
    line-height: 13.4px;
  }
  .about p + p { margin-top: 13px; }
  .contact {
    position: absolute;
    left: 559px; top: 962px;
    width: 301px; height: 188px;
    background: var(--contact-panel);
    border-radius: 6px 0 0 6px;
    box-sizing: border-box;
    padding: 10px 52px 0 0;
    text-align: right;
    color: var(--white);
  }
  .contact address {
    margin-top: 14px;
    font-style: normal;
    font-weight: 300;
    font-size: 16px;
    line-height: 22.5px;
  }
</style>
</head>
<body>
<div class="flyer">
  <div class="hero-photo" role="img" aria-label="Photo of a businessman in shirt and tie at a laptop in a bright boardroom"></div>

  <header class="masthead">
    <h1 class="masthead-name">RIDGEWAY<span class="masthead-sub">NETWORKING</span></h1>
    <p class="masthead-tagline">Complete IT management</p>
  </header>

  <div class="brand-mark">
    <span class="brand-square"></span>
    <span>Ridgeway Networking</span>
  </div>

  <h2 class="column-title col-1">WHAT WE DO</h2>
  <h2 class="column-title col-2">INSTALLATION</h2>
  <h2 class="column-title col-3">SUPPORT</h2>

  <div class="content-band"></div>

  <section class="card col-1">
    <p>Ridgeway Networking specialises in providing complete IT management for small to medium size business.</p>
    <p>We provide installation and maintenance of complete managed networks with a focus on ongoing management.</p>
    <p>Ridgeway works in a clear, concise and professional manner to ensure that every area of your business IT requirements are effectively managed.</p>
    <p>Allowing you the freedom to run your business</p>
  </section>

  <section class="card col-2">
    <svg width="0" height="0" style="position:absolute">
      <symbol id="tick" viewBox="0 0 10 10">
        <path d="M1 5.2 L4 8 L9 1.5" fill="none" stroke="#5b6e80" stroke-width="1.8"/>
      </symbol>
    </svg>
    <ul class="service-list">
      <li><svg class="tick"><use href="#tick"/></svg>Networking</li>
      <li><svg class="tick"><use href="#tick"/></svg>Servers</li>
      <li><svg class="tick"><use href="#tick"/></svg>Workstations</li>
      <li><svg class="tick"><use href="#tick"/></svg>Laptops</li>
      <li><svg class="tick"><use href="#tick"/></svg>Firewalls</li>
    </ul>
    <ul class="service-list">
      <li><svg class="tick"><use href="#tick"/></svg>Data Cabling</li>
      <li><svg class="tick"><use href="#tick"/></svg>All electrical Work</li>
      <li><svg class="tick"><use href="#tick"/></svg>Server Racks</li>
      <li><svg class="tick"><use href="#tick"/></svg>Network Infrastructure</li>
      <li><svg class="tick"><use href="#tick"/></svg>Off site back up</li>
    </ul>
    <ul class="service-list">
      <li><svg class="tick"><use href="#tick"/></svg>ADSL Connections</li>
      <li><svg class="tick"><use href="#tick"/></svg>Web Hosting</li>
      <li><svg class="tick"><use href="#tick"/></svg>Web Design</li>
      <li><svg class="tick"><use href="#tick"/></svg>Website Maintenance</li>
      <li><svg class="tick"><use href="#tick"/></svg>Domain Names PABX systems</li>
    </ul>
  </section>

  <section class="card col-3">
    <p>Unlike organisation who offer one level of service, Ridgeway Networking is equipped to offer a lage range of support agreements depending on your needs and budget.</p>
    <p>Whether you require ad-hoc support when things go wrong, or you're after complete seamless management of all your communications and technology equipment, Ridgeway has qualified and experienced staff to take care of your needs.</p>
    <p>Ridgeway Networking understands that things always malfunction at the least convenient time, so we offer hours support to make sure small problems don't turn into disasters.</p>
  </section>

  <section class="about">
    <h2 class="section-heading">ABOUT US</h2>
    <p>"Complete IT Management", discover the difference with Ridgeway Networking Located in Perth Western Australia, Ridgeway Networking specializes in providing complete IT Management for Small to Medium size Businesses. Ridgeway provides a unique all-encompassing approach to IT Management, differentiating it from other IT and Communications providers.</p>
    <p>Focusing on an in-depth understanding of our clients needs, Ridgeway approach to IT management allows us the opportunity to implement and support seamless IT and Communications environments. With over 20 years experience in the industry, Ridgeway covers the entire IT spectrum, from server environments and workstations through to cabling and phone systems.</p>
  </section>

  <section class="contact">
    <h2 class="section-heading">CONTACT US</h2>
    <address>
      22 / 18 Marlow Court<br>
      Westbrook, 6170<br>
      Phone: 9400 1357<br>
      www.ridgewaynet.com.au<br>
      info@ridgewaynet.com.au
    </address>
  </section>
</div>
</body>
</html>
```